Business Card Design - Ember Hill Lodge

We are looking at a new design for our business cards that has a modern and professional look. We run a residential aged care facility focussing on the care of residents. The cards will be used for potential clients, consultants and business opportunities in this sector. Blue and white is our main colours and would to see these colours incorporated in the design.
Industry/Entity Type
Business
Contact Information for Business Card
Ember Hill Lodge, Dean Marsh, dmarsh@emberhilllodge-mail.example, Finance Manager, 0491 372 608, BCom, 27 Marbury Way, Ashford Vale, Qld 4179.
Look and feel

```html
<!DOCTYPE html>
<html lang="en">
<head>
<meta charset="utf-8">
<title>Ember Hill Lodge – Business Card</title>
<link rel="stylesheet" href="https://fonts.googleapis.com/css2?family=Open+Sans:wght@400;600;800&display=swap">
<style>
  :root{
    --bg:#2b2b2d;
    --taupe:#aca39a;
    --white:#ffffff;
    --blue:#4a7e9c;
    --navy:#1d3a55;
    --ink:#2f4a63;
    --rule:#3f5f7a;
  }
  *{margin:0;padding:0;box-sizing:border-box}
  html,body{width:1200px;height:900px;overflow:hidden;background:var(--bg);font-family:"Open Sans",Arial,sans-serif}
  .canvas{position:relative;width:1200px;height:900px}
  .card{position:absolute;width:700px;height:400px;border-radius:26px;overflow:hidden}
  .card--back{left:110px;top:40px;background:var(--taupe)}
  .card--front{left:390px;top:470px;background:var(--white)}

  .brand{display:flex;align-items:center;gap:16px;color:var(--navy);font-weight:600;text-transform:uppercase;letter-spacing:2px;white-space:nowrap}
  .brand__dot{border-radius:50%;background:var(--blue);flex:none}
  .card--back .brand{position:absolute;left:50%;top:50%;transform:translate(-50%,-50%);font-size:32px}
  .card--back .brand__dot{width:70px;height:70px}
  .card--front .brand{position:absolute;right:40px;top:48px;font-size:21px;gap:12px}
  .card--front .brand__dot{width:46px;height:46px}

  .address{position:absolute;right:40px;top:205px;text-align:right;font-size:15px;line-height:21px;color:var(--ink);font-style:normal}
  .rule-long{position:absolute;left:232px;right:40px;top:258px;height:1.5px;background:var(--rule)}
  .person{position:absolute;left:40px;top:262px}
  .person__name{font-size:27px;font-weight:800;color:var(--navy);letter-spacing:.5px;line-height:30px;white-space:nowrap}
  .person__role{font-size:14px;color:var(--blue);letter-spacing:.3px;line-height:18px;white-space:nowrap}
  .rule-short{width:192px;height:1.5px;background:var(--rule);margin:5px 0 8px}
  .contacts{list-style:none;font-size:16px;color:var(--ink);line-height:24px}
  .contacts li{display:flex;align-items:center;gap:9px;white-space:nowrap}
  .contacts svg{width:13px;height:13px;flex:none}
</style>
</head>
<body>
<main class="canvas">
  <section class="card card--back">
    <div class="brand"><span class="brand__dot"></span>Ember Hill Lodge</div>
  </section>

  <section class="card card--front">
    <div class="brand"><span class="brand__dot"></span>Ember Hill Lodge</div>

    <address class="address">27 Marbury Way<br>Ashford Vale, Qld 4179</address>
    <div class="rule-long"></div>

    <div class="person">
      <h1 class="person__name">DEAN MARSH</h1>
      <p class="person__role">FINANCE MANAGER(BCOM)</p>
      <div class="rule-short"></div>
      <ul class="contacts">
        <li>
          <svg viewBox="0 0 24 24" aria-hidden="true"><path fill="#3f5f7a" d="M6.6 10.8c1.4 2.8 3.8 5.1 6.6 6.6l2.2-2.2c.3-.3.7-.4 1-.2 1.1.4 2.3.6 3.6.6.6 0 1 .4 1 1V20c0 .6-.4 1-1 1C10.6 21 3 13.4 3 4c0-.6.4-1 1-1h3.5c.6 0 1 .4 1 1 0 1.3.2 2.5.6 3.6.1.3 0 .7-.2 1z"/></svg>
          0491 372 608
        </li>
        <li>
          <svg viewBox="0 0 24 24" aria-hidden="true"><rect x="2.5" y="5" width="19" height="14" rx="1.5" fill="none" stroke="#3f5f7a" stroke-width="2"/><path d="M3 6l9 7 9-7" fill="none" stroke="#3f5f7a" stroke-width="2"/></svg>
          dmarsh@emberhilllodge-mail.example
        </li>
      </ul>
    </div>
  </section>
</main>
</body>
</html>
```